Website Redesign for a Bar Association

Design a user-friendly website that promotes the most important content and drives user engagement. Directional site map (navigation & content flow) document attached.

Existing Website: http://harrowfieldlaw.org/

Competitive Site Inspiration:
https://www.tevonlaw.org
https://www.pqlegal.org

Must use one of the following Blogforge themes:
https://zarplates.com/lite/?theme=gazette_lite
https://preview.plinkora.com/?demo=brisknews

Industry/Entity Type

Legal

Font styles to use
Serif
Sans Serif

Colors
0355a3
f37122

Requirements
Must have
• HLS Logo

```html
<!DOCTYPE html>
<html lang="en">
<head>
<meta charset="utf-8">
<title>Harrowfield Law Society</title>
<link href="https://fonts.googleapis.com/css2?family=Lato:wght@400;700;900&family=Open+Sans:wght@400;700&family=Oswald:wght@500;700&display=swap" rel="stylesheet">
<style>
:root{
  --orange:#f37122;
  --navy:#2c3a62;
  --navy-dark:#243153;
  --rule:#e2463f;
  --ink:#222;
  --text:#333;
  --muted:#9a9a9a;
  --panel:#f1f1f1;
  --footer:#2b2b2b;
  --footer-deep:#232323;
  --page-bg:#161616;
  --blue:#2a47b5;
  --sky:#1ea8ec;
}
*{margin:0;padding:0;box-sizing:border-box}
html,body{width:1200px;height:2369px;overflow:hidden}
body{background:radial-gradient(ellipse at 50% 40%,#3a3a3a 0%,#1d1d1d 55%,var(--page-bg) 100%);font-family:'Lato',sans-serif;color:var(--text);position:relative}
.site{position:absolute;left:120px;top:21px;width:961px;height:2330px;background:#fff}
.abs{position:absolute}

/* header */
.brand{left:14px;top:38px;display:flex;align-items:center;gap:12px}
.brand-mark{width:66px;height:66px;border-radius:50%;background:var(--navy)}
.brand-name{font-family:'Lato',sans-serif;font-weight:900;color:var(--navy);line-height:1;font-size:30px;letter-spacing:.5px}
.brand-name span{display:block;font-size:20px;margin-top:4px}
.header-actions{right:26px;top:45px;display:flex;gap:2px}
.header-actions a{display:block;height:35px;line-height:35px;padding:0 13px;font-size:11px;font-weight:700;color:#fff;text-decoration:none;text-transform:uppercase}
.btn-donate{background:var(--orange);width:93px;text-align:center}
.btn-login{background:var(--navy)}

.nav{left:0;top:126px;width:961px;height:37px;background:var(--navy);border-bottom:5px solid var(--orange);box-sizing:content-box;display:flex}
.nav a{display:flex;align-items:center;gap:7px;height:37px;padding:0 11px;color:#fff;font-size:12px;font-weight:700;text-decoration:none;text-transform:uppercase;border-right:1px solid #3f4d74}
.nav a.current{background:var(--orange);border-right:none}
.nav .caret{width:6px;height:6px;border-right:1.5px solid #fff;border-bottom:1.5px solid #fff;transform:rotate(45deg);margin-top:-3px}

/* section heads */
.head{font-weight:700;font-size:14px;color:var(--ink);text-transform:uppercase;border-bottom:2px solid var(--rule);padding-bottom:5px}
.head.accent{color:var(--orange)}

/* slider */
.slider{left:22px;top:188px;width:603px;height:340px;background:linear-gradient(160deg,#3b4466 0%,#2a3150 45%,#1b2039 100%)}
.dots{position:absolute;left:237px;bottom:16px;display:flex;gap:11px}
.dots i{width:13px;height:13px;border-radius:50%;background:#fff;display:block}
.dots i.on{background:var(--rule)}

/* program cards */
.card{width:290px}
.card .photo{display:block;width:286px;height:110px;margin:8px 0 0 2px}
.card p{font-size:12px;line-height:21.5px;text-align:justify;margin:12px 14px 0 3px}
.btn{display:inline-block;background:var(--navy);color:#fff;font-size:10.5px;height:23px;line-height:23px;padding:0 7px;text-decoration:none;margin:18px 0 0 4px}
.card-rule{position:absolute;height:1px;background:#eee;width:290px}

.committees{left:370px;top:1203px;width:220px}
.committees h2{font-family:'Lato',sans-serif;font-weight:900;color:var(--orange);font-size:24px;text-align:center}
.committees .bar{width:76px;margin:7px auto 0;border-top:2px solid var(--navy);border-bottom:2px solid var(--navy);height:5px}
.committees .lead{font-size:12px;font-weight:700;color:#444;line-height:20px;text-align:justify;margin-top:24px}
.committees .body{font-size:11.5px;color:#666;line-height:20px;text-align:justify;margin:8px 0 0 4px;letter-spacing:.3px}

/* about */
.about-box{left:22px;top:1548px;width:603px;height:90px;background:linear-gradient(90deg,#f4f4f4,#fafafa);padding:7px 12px}
.about-box h3{font-size:14px;font-weight:700;color:var(--ink)}
.about-box p{font-size:12px;line-height:21.5px;margin-top:9px;color:#333}
.about-photo{left:26px;top:1663px;width:593px;height:331px;background:linear-gradient(135deg,#5a3e2a 0%,#8a5a33 40%,#b67a40 65%,#3b2e25 100%)}

/* sidebar */
.side{left:648px;width:290px}
.search-panel{left:648px;top:234px;width:290px;height:60px;background:var(--panel);padding:15px 28px}
.search-panel .field{height:30px;background:#fff;border:1px solid #e3e3e3;font-size:9px;color:#888;padding:9px 8px;font-family:'Open Sans',sans-serif}
.promo{left:651px;top:365px;width:284px;height:191px;background:linear-gradient(180deg,#2a3fa8 0%,#2c4dbf 70%);text-align:center;font-family:'Oswald',sans-serif;color:#fff;overflow:hidden}
.promo .l1{margin-top:36px;color:#f3c020;font-size:14px;font-weight:500;letter-spacing:-.2px}
.promo .l2{font-size:14px;font-weight:500;margin-top:1px}
.promo .l3{font-size:44px;font-weight:700;line-height:46px;letter-spacing:-.5px}
.promo .l4{font-size:12px;font-weight:500}
.promo .l4 b{color:#f3c020;font-weight:500}
.promo .foot{position:absolute;left:0;bottom:0;width:100%;height:50px;background:var(--sky);font-size:19px;font-weight:500;line-height:46px;letter-spacing:-.3px}

.news{left:648px;top:664px;width:292px}
.news-item{display:flex;gap:14px;height:90px;border-bottom:1px solid #eee;padding-top:2px;margin-bottom:0}
.news-item + .news-item{padding-top:9px}
.news-thumb{width:71px;height:53px;flex:none}
.news-item h4{font-family:'Open Sans',sans-serif;font-size:13px;font-weight:700;color:#111;line-height:16px;margin-top:0}
.meta{font-family:'Open Sans',sans-serif;font-size:9.5px;color:var(--muted);display:flex;align-items:center;gap:4px;margin-top:3px}
.meta svg{flex:none}
.meta .gap{width:6px}

.donate-wrap{left:648px;top:1209px;width:290px;height:240px;background:var(--panel);padding:8px 11px}
.donate{width:268px;height:223px;background:linear-gradient(135deg,#f0661c 0%,#f47a1e 50%,#e85d14 100%);text-align:center;color:#fff;padding-top:64px}
.donate .t1{font-size:14px;font-weight:700}
.donate .t2{font-size:17px;margin-top:6px}
.donate .t3{font-size:18px;font-weight:900;margin-top:5px}
.donate a{display:inline-block;margin-top:14px;background:var(--navy-dark);color:#fff;text-decoration:none;font-size:13px;padding:0 11px;height:30px;line-height:30px}

/* footer */
.footer{left:0;top:2038px;width:961px;height:250px;background:var(--footer)}
.fcol{position:absolute;top:22px;width:212px;color:#ddd}
.fcol h5{font-size:13px;font-weight:700;text-transform:uppercase;color:#fff;border-bottom:2px solid var(--rule);padding-bottom:5px}
.fcol ul{list-style:none;margin-top:10px}
.fcol li{font-size:12px;height:28.5px;line-height:28px;border-bottom:1px solid #3c3c3c}
.fcol p{font-size:12px;line-height:19px;margin-top:12px}
.copyright{left:0;top:2290px;width:961px;height:40px;background:var(--footer-deep);border-top:2px solid #555;color:#bbb;font-size:11px;padding:13px 22px}
</style>
</head>
<body>
<div class="site">

  <header>
    <div class="abs brand">
      <div class="brand-mark"></div>
      <div class="brand-name">HARROWFIELD<span>LAW SOCIETY</span></div>
    </div>
    <div class="abs header-actions">
      <a class="btn-donate" href="#">Donate</a>
      <a class="btn-login" href="#">Member Login</a>
    </div>
    <nav class="abs nav">
      <a class="current" href="#">Home</a>
      <a href="#">About <i class="caret"></i></a>
      <a href="#">Member Resources <i class="caret"></i></a>
      <a href="#">Programs <i class="caret"></i></a>
      <a href="#">Scholarships <i class="caret"></i></a>
      <a href="#">Community Resources <i class="caret"></i></a>
      <a href="#">News &amp; Events</a>
      <a href="#" style="border-right:none">Contact</a>
    </nav>
  </header>

  <main>
    <div class="abs slider" role="img" aria-label="Stone columns of a courthouse facade in navy tones">
      <div class="dots"><i class="on"></i><i></i><i></i><i></i><i></i></div>
    </div>

    <article class="abs card" style="left:23px;top:552px">
      <h2 class="head">Law School Pipeline Program</h2>
      <div class="photo" role="img" aria-label="Students seated in a courtroom gallery" style="background:linear-gradient(120deg,#5a3a28,#a9744e 50%,#d9b491)"></div>
      <p>The Law School Pipeline Program (LSPP) aims to reduce hurdles to law school enrollment for underrepresented students with the help of Lantern Test Prep...</p>
      <a class="btn" href="#">Learn More</a>
    </article>
    <article class="abs card" style="left:335px;top:552px">
      <h2 class="head">Summer Clerkship Program</h2>
      <div class="photo" role="img" aria-label="Students writing at desks during class" style="background:linear-gradient(120deg,#4a5a78,#8a7a6c 50%,#d8c4a8)"></div>
      <p>The SCP Committee coordinates the Harrowfield Law Society's annual summer clerkship program, which is designed to increase the number of minority attorneys employed as partners; associates...</p>
      <a class="btn" href="#">Learn More</a>
    </article>
    <div class="card-rule" style="left:23px;top:846px"></div>
    <div class="card-rule" style="left:335px;top:846px"></div>

    <article class="abs card" style="left:23px;top:870px">
      <h2 class="head">Judicial Externship Program</h2>
      <div class="photo" role="img" aria-label="Close view of open book pages" style="background:linear-gradient(110deg,#e9dcb6,#cbb27c 60%,#9b7f4c)"></div>
      <p style="margin-top:18px">JEP seeks to increase the representation of minority law school graduates among the ranks of judicial clerks. The JEP Program achieves this goal by helping well-qualified minority law students...</p>
      <a class="btn" href="#">Learn More</a>
    </article>
    <article class="abs card" style="left:335px;top:870px">
      <h2 class="head accent">Pipeline Programs</h2>
      <div class="photo" role="img" aria-label="Criminal law book beside a gavel" style="background:linear-gradient(100deg,#2f5a9a 0%,#3f6aa8 48%,#7a4a2c 55%,#4a2a1c 100%)"></div>
      <p style="margin-top:18px">The Pipeline Committee is responsible for developing educational programming targeted at middle school and high school students and creating initiatives to ensure a pathway to success...</p>
      <a class="btn" href="#">Learn More</a>
    </article>
    <div class="card-rule" style="left:23px;top:1163px"></div>
    <div class="card-rule" style="left:335px;top:1163px"></div>

    <article class="abs card" style="left:23px;top:1187px">
      <h2 class="head">Minority Bar Passage Program</h2>
      <div class="photo" role="img" aria-label="Exam takers writing at rows of desks" style="background:linear-gradient(110deg,#c9a983,#dcd2c4 50%,#6f7682)"></div>
      <p>The Marcus Ellery Minority Bar Passage Program (MBPP) is designed to improve bar passage rates of law school graduates sitting for the Michigan Bar Exam...</p>
      <a class="btn" href="#">Learn More</a>
    </article>

    <section class="abs committees">
      <h2>HLS Committees</h2>
      <div class="bar"></div>
      <p class="lead">Are you looking for a way to be more involved in HLS activities? Find the committee that is right for you!</p>
      <p class="body">The HLS's committees keep members informed of significant developments in their areas of practice and shape association policy on issues of professional concern.</p>
      <a class="btn" href="#" style="margin:18px 0 0 6px">Learn More</a>
    </section>

    <h2 class="abs head" style="left:23px;top:1514px;width:603px">About HL Society</h2>
    <div class="abs about-box">
      <h3>The Harrowfield Law Society is an active affiliate of the National Counsel Alliance</h3>
      <p>The Harrowfield Law Society was established by a number of African-American attorneys during the 1930's. It was organized to coordinate the energies and talents of the increasing number of African-Americans admitted to practice throughout Michigan.</p>
    </div>
    <div class="abs about-photo" role="img" aria-label="Members meeting around a conference table with laptops"></div>
  </main>

  <aside>
    <h2 class="abs head side" style="top:192px">Search</h2>
    <div class="abs search-panel"><div class="field">SEARCH ...</div></div>

    <h2 class="abs head side" style="top:317px;padding-left:2px">Public Resources</h2>
    <div class="abs promo">
      <div class="l1">INTRODUCING THE ALL-NEW</div>
      <div class="l2">MARLOW COUNTY CLERK'S OFFICE</div>
      <div class="l3">eBOOKER</div>
      <div class="l4">EASY AS <b>1-2-3</b>. PREPARE. <b>APPLY.</b> SCHEDULE.</div>
      <div class="foot">MARLOW COUNTY CLERK, DENISE R. HOLLAND</div>
    </div>

    <h2 class="abs head side" style="top:624px;padding-left:2px">Latest News</h2>
    <div class="abs news">
      <div class="news-item"><div class="news-thumb" role="img" aria-label="Spa flowers and towels" style="background:linear-gradient(135deg,#e8e0d2,#d27a2e)"></div><div><h4>Indulge yourself</h4><div class="meta"><svg width="9" height="9" viewBox="0 0 10 10"><circle cx="5" cy="5" r="4" fill="none" stroke="#9a9a9a"/><path d="M5 2.5V5h2" stroke="#9a9a9a" fill="none"/></svg>January 12, 2015<span class="gap"></span><svg width="10" height="9" viewBox="0 0 12 10"><path d="M1 1h10v6H5L2 9V7H1z" fill="none" stroke="#9a9a9a"/></svg>0</div></div></div>
      <div class="news-item"><div class="news-thumb" role="img" aria-label="Colorful festival decorations" style="background:linear-gradient(135deg,#2f7a3a,#c8342c 50%,#e6b12c)"></div><div><h4>Colorful entertainment from India</h4><div class="meta"><svg width="9" height="9" viewBox="0 0 10 10"><circle cx="5" cy="5" r="4" fill="none" stroke="#9a9a9a"/><path d="M5 2.5V5h2" stroke="#9a9a9a" fill="none"/></svg>January 11, 2015<span class="gap"></span><svg width="10" height="9" viewBox="0 0 12 10"><path d="M1 1h10v6H5L2 9V7H1z" fill="none" stroke="#9a9a9a"/></svg>0</div></div></div>
      <div class="news-item"><div class="news-thumb" role="img" aria-label="Yacht on blue water" style="background:linear-gradient(180deg,#6aa3d0,#1f4f86)"></div><div><h4>Huge takeover in boat industry</h4><div class="meta"><svg width="9" height="9" viewBox="0 0 10 10"><circle cx="5" cy="5" r="4" fill="none" stroke="#9a9a9a"/><path d="M5 2.5V5h2" stroke="#9a9a9a" fill="none"/></svg>January 10, 2015<span class="gap"></span><svg width="10" height="9" viewBox="0 0 12 10"><path d="M1 1h10v6H5L2 9V7H1z" fill="none" stroke="#9a9a9a"/></svg>0</div></div></div>
      <div class="news-item"><div class="news-thumb" role="img" aria-label="Coastal highland cliffs" style="background:linear-gradient(180deg,#b89a6a,#4f6a3a)"></div><div><h4>Time out in the scottish highlands</h4><div class="meta"><svg width="9" height="9" viewBox="0 0 10 10"><circle cx="5" cy="5" r="4" fill="none" stroke="#9a9a9a"/><path d="M5 2.5V5h2" stroke="#9a9a9a" fill="none"/></svg>January 9, 2015<span class="gap"></span><svg width="10" height="9" viewBox="0 0 12 10"><path d="M1 1h10v6H5L2 9V7H1z" fill="none" stroke="#9a9a9a"/></svg>0</div></div></div>
      <div class="news-item"><div class="news-thumb" role="img" aria-label="Concert stage in dim light" style="background:linear-gradient(135deg,#1c1c1c,#6c6c6c)"></div><div><h4>Dana Whitlock's comeback</h4><div class="meta"><svg width="9" height="9" viewBox="0 0 10 10"><circle cx="5" cy="5" r="4" fill="none" stroke="#9a9a9a"/><path d="M5 2.5V5h2" stroke="#9a9a9a" fill="none"/></svg>January 8, 2015<span class="gap"></span><svg width="10" height="9" viewBox="0 0 12 10"><path d="M1 1h10v6H5L2 9V7H1z" fill="none" stroke="#9a9a9a"/></svg>0</div></div></div>
      <div class="news-item"><div class="news-thumb" role="img" aria-label="Tropical beach with palm leaves" style="background:linear-gradient(180deg,#7a9a3a,#3ec1d8 55%,#eee2c6)"></div><div><h4>Relax at the best beaches worldwide</h4><div class="meta"><svg width="9" height="9" viewBox="0 0 10 10"><circle cx="5" cy="5" r="4" fill="none" stroke="#9a9a9a"/><path d="M5 2.5V5h2" stroke="#9a9a9a" fill="none"/></svg>January 7, 2015<span class="gap"></span><svg width="10" height="9" viewBox="0 0 12 10"><path d="M1 1h10v6H5L2 9V7H1z" fill="none" stroke="#9a9a9a"/></svg>0</div></div></div>
    </div>

    <div class="abs donate-wrap">
      <div class="donate">
        <div class="t1">Donate to the Harrowfield</div>
        <div class="t2">Law Foundation support our</div>
        <div class="t3">PROGRAMS &amp; SCHOLARSHIPS</div>
        <a href="#">DONATE NOW</a>
      </div>
    </div>
  </aside>

  <footer class="abs footer">
    <div class="fcol" style="left:22px">
      <h5>Recent Posts</h5>
      <ul><li>Annual festival of lights</li><li>JR's new collection out</li><li>Offering showrooms for exhibitions</li><li>Cinema complex reopening</li><li>Photoshoot at home</li><li>Effective kissing with lipstick</li></ul>
    </div>
    <div class="fcol" style="left:257px">
      <h5>Do You Like This?</h5>
      <ul><li>Full features overview</li><li>Upgrade to Premium</li><li>More themes by Zarplates</li><li>Become a fan on Friendhub</li><li>Follow us on Chirper</li></ul>
    </div>
    <div class="fcol" style="left:492px">
      <h5>Categories</h5>
      <ul><li>Beauty</li><li>Business</li><li>Entertainment</li><li>Lifestyle</li><li>Travel</li><li>World</li></ul>
    </div>
    <div class="fcol" style="left:726px">
      <h5>Questions?</h5>
      <p>If you have any questions regarding this free Blogforge theme, don't hesitate to contact us via Friendhub, Chirper or our website. We love to get feedback and we will do our best to make you happy.</p>
    </div>
  </footer>
  <div class="abs copyright">Copyright © 2020 | Blogforge Theme by Zarplates</div>
</div>
</body>
</html>
```